Loyalty Program

I would like to have a flyer designed to promote and explain our loyalty program targeting the local customers purchasing stationery, which then a percentage goes to the local schools in the form of Craft Products for the school children to use in their projects.
Thought of calling it :" Paper Pals" but open to other ideas
Regards
Derek

Target Market(s)

The idea is to have parents of the children at schools purchase more stationery locally, which will then give more craft and stationery resources for the children to use at school. To save parents and teachers the extra expense of buying extra school supplies during the year.

Industry/Entity Type

School

Requirements
Must have
• . Community focus
. Helping the children learn and develop creative skills
. Simple one page flyer

```html
<!DOCTYPE html>
<html lang="en">
<head>
<meta charset="utf-8">
<title>Paper Pals – Harbourside News Agency Loyalty Programme</title>
<link rel="stylesheet" href="https://fonts.googleapis.com/css2?family=Arimo:wght@400;700&display=swap">
<style>
  :root {
    --flyer-yellow: #fff200;
    --flyer-red: #ee1c24;
    --ink: #111111;
    --paper: #ffffff;
    --dot-magenta: #ec1c8c;
    --dot-yellow: #ffe600;
    --dot-cyan: #22b8e8;
    --clip-blue: #3a78c8;
    --clip-green: #3f9a4a;
    --clip-pink: #f2a6b8;
  }
  * { margin: 0; padding: 0; box-sizing: border-box; }
  html, body { width: 927px; height: 1200px; overflow: hidden; background: var(--paper); }
  .flyer {
    position: relative;
    width: 927px;
    height: 1200px;
    overflow: hidden;
    background: var(--flyer-yellow);
    font-family: "Arimo", Arial, sans-serif;
    color: var(--ink);
  }
  .hero { position: absolute; left: 0; top: 0; width: 927px; height: 684px; display: block; }
  .hero-title { font-family: "Arimo", Arial, sans-serif; font-weight: 700; }
  .store-badge {
    position: absolute;
    left: 622px; top: 365px;
    width: 280px; height: 280px;
    border-radius: 50%;
    background: var(--paper);
    display: flex; flex-direction: column; align-items: center; justify-content: center;
    text-align: center;
  }
  .store-badge__name {
    font-weight: 700; font-size: 25px; line-height: 1.05;
    color: var(--ink); letter-spacing: 0.5px;
  }
  .store-badge__details {
    margin-top: 10px; font-size: 10.5px; line-height: 1.35; color: var(--ink);
  }
  .offer { position: absolute; left: 70px; top: 696px; width: 830px; }
  .offer__heading { font-weight: 400; font-size: 49px; line-height: 62px; }
  .offer__body { margin-top: 14px; margin-left: 3px; font-size: 22px; line-height: 31px; width: 690px; }
  .contact { position: absolute; left: 70px; top: 1044px; font-size: 16px; line-height: 21px; font-style: normal; }
  .accent-stripes { position: absolute; left: 0; top: 684px; width: 927px; height: 516px; }
</style>
</head>
<body>
<main class="flyer">
  <svg class="hero" viewBox="0 0 927 684" xmlns="http://www.w3.org/2000/svg">
    <defs>
      <linearGradient id="halftoneTones" x1="0" y1="0" x2="1" y2="1">
        <stop offset="0" stop-color="var(--dot-yellow)"/>
        <stop offset="0.4" stop-color="var(--dot-magenta)" stop-opacity="0.75"/>
        <stop offset="0.7" stop-color="var(--dot-cyan)" stop-opacity="0.6"/>
        <stop offset="1" stop-color="var(--flyer-red)"/>
      </linearGradient>
      <linearGradient id="clipTones" x1="0" y1="0" x2="1" y2="1">
        <stop offset="0" stop-color="var(--clip-green)"/>
        <stop offset="0.35" stop-color="var(--clip-blue)"/>
        <stop offset="0.65" stop-color="var(--clip-pink)"/>
        <stop offset="1" stop-color="var(--dot-yellow)"/>
      </linearGradient>
    </defs>
    <rect class="hero__paper" width="927" height="684" fill="var(--paper)"/>
    <polygon class="hero__halftone" role="img" aria-label="Colourful halftone dot pattern in magenta, yellow, cyan and red"
             points="0,0 150,0 175,180 230,610 0,640" fill="url(#halftoneTones)" opacity="0.85"/>
    <polygon class="hero__photo" role="img" aria-label="Photo of scattered coloured paper clips in blue, green, pink and yellow"
             points="0,658 927,92 927,676 0,676" fill="url(#clipTones)" opacity="0.8"/>
    <polygon class="hero__band" points="0,618 927,48 927,94 0,662" fill="var(--flyer-red)"/>
    <polygon class="hero__corner" points="880,0 927,0 927,22" fill="var(--flyer-red)"/>
    <rect class="hero__divider" x="0" y="676" width="927" height="8" fill="var(--flyer-red)"/>
    <text class="hero-title" x="228" y="405" transform="rotate(-33 228 405)" font-size="92"
          fill="var(--ink)" textLength="610" lengthAdjust="spacingAndGlyphs">PAPER PALS</text>
  </svg>

  <div class="store-badge">
    <div class="store-badge__name">HARBOURSIDE<br>NEWS AGENCY</div>
    <div class="store-badge__details">
      Shop 4 / 118 Wattle Rd, Harbourside 4069<br>
      Ph: 07 55501234<br>
      email: harbourside_news@mailbox.com.au
    </div>
  </div>

  <svg class="accent-stripes" viewBox="0 0 927 516" xmlns="http://www.w3.org/2000/svg" aria-hidden="true">
    <polygon points="927,244 927,268 590,516 558,516" fill="var(--flyer-red)"/>
    <polygon points="927,420 927,516 800,516" fill="var(--flyer-red)"/>
  </svg>

  <section class="offer">
    <h1 class="offer__heading">Join our loyalty programme today<br>and help local schools!</h1>
    <p class="offer__body">Harbourside News Agency would like to invite all of our local customers to join our loyalty programme! Here at Harbourside we are helping out local schools by donating a percentage of your purchases to local schools.<br>We do this by supplying the school with crafts products to help them with the kids with their projects.</p>
  </section>

  <address class="contact">
    Shop 4/118 Wattle Rd, Harbourside 4069<br>
    Ph: 0755501234<br>
    email: harbourside_news@mailbox.com.au
  </address>
</main>
</body>
</html>
```